Brambel Logging Business Card Design Project

We need a new company business card. We provide professional timber harvesting (logging) and forest management services. I'm open to any creative design. Most company caps and shirts are navy blue and Light grey. Logo does not necessarily have to contain those colors. Logo containing picture of logging equipment, log truck, trees, or logs are acceptable. Be creative. Final logo should communicate our company's pride and professionalism in the East Texas Timber Industry.
Updates

Target Market(s)

Timber owners, sawmills, and forestry professionals

Industry/Entity Type

Business

Requirements
Must have
• Must have Contact Info.
Phone: 936-402-5817
address: PO Box 8462
New Waverly, Tx 77358
www.mbrambellogging.example
mbrambellogging@mailbox.example
Owner: Marv Brambel

Or design must leave room for this info.

```html
<!DOCTYPE html>
<html lang="en">
<head>
<meta charset="utf-8">
<title>Brambel Logging – Business Card</title>
<link href="https://fonts.googleapis.com/css2?family=Michroma&display=swap" rel="stylesheet">
<style>
  :root {
    --backdrop: #d9dadb;
    --card: #ffffff;
    --ink: #2b2b2d;
    --muted: #5a5a5e;
    --red: #d9262c;
    --charcoal: #353538;
    --rule: #b9b9bd;
  }
  * { box-sizing: border-box; margin: 0; padding: 0; }
  html, body {
    width: 1200px; height: 771px; overflow: hidden;
    background: var(--backdrop);
  }
  .card {
    position: absolute; left: 75px; top: 85px;
    width: 1050px; height: 600px;
    background: var(--card);
    overflow: hidden;
    box-shadow: 0 6px 24px rgba(0,0,0,.18);
    font-family: "Michroma", "Arial", sans-serif;
    color: var(--ink);
  }
  .card__bands { position: absolute; inset: 0; width: 100%; height: 100%; }
  .brand {
    position: absolute; left: 330px; top: 120px;
    display: flex; align-items: center; gap: 26px;
  }
  .brand__names { color: var(--ink); line-height: 1.15; text-transform: uppercase; }
  .brand__owner { font-size: 26px; letter-spacing: 1px; }
  .brand__company { font-size: 40px; letter-spacing: 1px; }
  .brand__mark { width: 46px; height: 46px; background: var(--red); }
  .contact {
    position: absolute; left: 300px; top: 300px;
    display: flex; gap: 22px;
  }
  .contact__person {
    text-align: right; width: 290px; padding-top: 4px;
    font-size: 15px; line-height: 1.55; color: var(--muted);
  }
  .contact__name { color: var(--red); font-size: 17px; letter-spacing: 1px; }
  .contact__title { margin-bottom: 14px; }
  .contact__divider { width: 1px; background: var(--rule); }
  .contact__list { list-style: none; font-size: 14px; line-height: 1; }
  .contact__item { display: flex; align-items: center; gap: 10px; height: 30px; }
  .contact__icon { width: 20px; height: 20px; flex: none; }
</style>
</head>
<body>
  <article class="card">
    <svg class="card__bands" viewBox="0 0 1050 600" aria-hidden="true">
      <path d="M0 280 C200 380 400 480 580 600 L0 600 Z" fill="var(--red)"/>
      <path d="M300 600 C560 540 820 520 1050 530 L1050 600 Z" fill="var(--charcoal)"/>
    </svg>

    <header class="brand">
      <div class="brand__names">
        <div class="brand__owner">Marv Brambel</div>
        <div class="brand__company">Brambel Logging</div>
      </div>
      <div class="brand__mark"></div>
    </header>

    <section class="contact">
      <div class="contact__person">
        <div class="contact__name">ALEX SAMPLE</div>
        <div class="contact__title">Owner / C.E.O</div>
        <div class="contact__address">Suite # 000, Sample Bldg,<br>XX 00000</div>
      </div>
      <div class="contact__divider"></div>
      <ul class="contact__list">
        <li class="contact__item">
          <svg class="contact__icon" viewBox="0 0 20 20"><circle cx="10" cy="10" r="10" fill="var(--red)"/><path d="M7 5l2 3-1.2 1.2a7 7 0 0 0 3 3L12 11l3 2-1 2c-4 0-9-5-9-9z" fill="#fff"/></svg>
          555-0100-000
        </li>
        <li class="contact__item">
          <svg class="contact__icon" viewBox="0 0 20 20"><circle cx="10" cy="10" r="10" fill="var(--red)"/><rect x="7" y="4" width="6" height="12" rx="1.5" fill="#fff"/></svg>
          555-0100-001
        </li>
        <li class="contact__item">
          <svg class="contact__icon" viewBox="0 0 20 20"><circle cx="10" cy="10" r="10" fill="var(--red)"/><rect x="5" y="7" width="10" height="8" fill="#fff"/><rect x="7" y="4" width="6" height="3" fill="#fff"/></svg>
          555-0100-002
        </li>
        <li class="contact__item">
          <svg class="contact__icon" viewBox="0 0 20 20"><circle cx="10" cy="10" r="10" fill="var(--red)"/><rect x="5" y="6" width="10" height="8" fill="#fff"/><path d="M5 6l5 4 5-4" fill="none" stroke="var(--red)" stroke-width="1.2"/></svg>
          mbrambellogging@mailbox.example
        </li>
        <li class="contact__item">
          <svg class="contact__icon" viewBox="0 0 20 20"><circle cx="10" cy="10" r="10" fill="var(--red)"/><circle cx="10" cy="10" r="5" fill="none" stroke="#fff" stroke-width="1.5"/><path d="M5 10h10M10 5v10" stroke="#fff" stroke-width="1.2"/></svg>
          www.mbrambellogging.example
        </li>
      </ul>
    </section>
  </article>
</body>
</html>
```